Shop front signage design for Bubble Tea Shop

Plum Harbor is Sydney based Green Tea Shop.We are looking for a modern and sleek signage for shop front end. We have Aluminium Composite Panel and Awning sign at the shop front. We will keep Aluminium composite panel simple with logo and text. We are after awning design which is above glass door and under the panel. Old Awning is PVC foam in two pieces 2310mm w x 1000mm h. We need someone to design awing. It should reflect Bubble tea and using bubble tea cups with pearls is essential. Stock images can be used. Avoid using icons or illustrative icons as we are after real images of bubble tea cup. This is to ensure that the brand is not taken as juice shop or cafe.
Panel Dimensions is 5250 mm w x 580 mm h.Awning/ Fascia sign is 4720 mm w x 1000 mm h.
Logo and signage concept is attached.

Target Market(s)

Corporate Male and Female, school, general public.

Colors
f36e22
333333
000000
eaeaea
cbcbcb

Requirements
Must have
• Bubble tea cups with fruit or milk tea.
Should not have
• Icons, illustration

```html
<!DOCTYPE html>
<html lang="en">
<head>
<meta charset="utf-8">
<title>Plum Harbor – Awning Sign</title>
<link href="https://fonts.googleapis.com/css2?family=Lobster&family=Nunito:wght@800&family=Rye&display=swap" rel="stylesheet">
<style>
  :root {
    --page-bg: #e6e6e6;
    --orange-deep: #f5a01c;
    --orange-mid: #f9c35c;
    --cream: #fdd998;
    --cream-light: #fde3b2;
    --brand-orange: #f36e22;
    --script-red: #e8472a;
    --shadow-brown: #4a2410;
    --ink: #000000;
    --arc-orange: #f5a623;
    --swoosh: #ffffff;
  }
  html, body {
    margin: 0;
    padding: 0;
    width: 1200px;
    height: 480px;
    overflow: hidden;
    background: var(--page-bg);
  }
  .canvas {
    position: relative;
    width: 1200px;
    height: 480px;
  }
  .awning {
    position: absolute;
    left: 0;
    top: 113px;
    width: 1200px;
    height: 254px;
    overflow: hidden;
    background: linear-gradient(90deg, var(--orange-deep) 0%, var(--orange-mid) 28%, var(--cream) 55%, var(--cream-light) 75%);
  }
  .brand {
    position: absolute;
    left: 44px;
    top: 30px;
    display: flex;
    align-items: center;
    gap: 10px;
  }
  .brand-dot {
    width: 44px;
    height: 44px;
    border-radius: 50%;
    background: var(--ink);
  }
  .brand-name {
    font-family: "Nunito", sans-serif;
    font-weight: 800;
    font-size: 28px;
    color: var(--ink);
    letter-spacing: -0.5px;
  }
  .cups-photo {
    position: absolute;
    left: 38px;
    top: 108px;
    width: 290px;
    height: 146px;
    border-radius: 6px;
    background: linear-gradient(90deg, #f4b070 0%, #9c86b8 30%, #f1b5bf 60%, #b6cf8e 85%, #f2e6d8 100%);
    opacity: 0.85;
  }
  .decor {
    position: absolute;
    inset: 0;
  }
  .headline {
    position: absolute;
    left: 390px;
    top: 0;
    width: 440px;
    height: 254px;
    margin: 0;
    text-align: center;
  }
  .headline-fresh {
    position: absolute;
    left: 0;
    right: 0;
    top: 2px;
    display: block;
    font-family: "Lobster", cursive;
    font-weight: 400;
    font-size: 108px;
    line-height: 1;
    color: var(--script-red);
    text-shadow: 2px 2px 0 rgba(120, 40, 10, 0.3);
  }
  .headline-product {
    position: absolute;
    left: 0;
    right: 0;
    top: 158px;
    display: block;
    font-family: "Rye", serif;
    font-weight: 400;
    font-size: 46px;
    line-height: 1;
    white-space: nowrap;
    color: var(--brand-orange);
    text-shadow: 2px 2px 0 var(--shadow-brown);
  }
</style>
</head>
<body>
<div class="canvas">
  <section class="awning">
    <svg class="decor" width="1200" height="254" viewBox="0 0 1200 254">
      <defs>
        <linearGradient id="drinks-tone" x1="0" y1="0" x2="1" y2="1">
          <stop offset="0" stop-color="#d9d9e0"/>
          <stop offset="0.45" stop-color="#f3d46a"/>
          <stop offset="0.75" stop-color="#f0a6b4"/>
          <stop offset="1" stop-color="#f4f1ef"/>
        </linearGradient>
      </defs>
      <path class="swoosh" d="M338 186 Q520 118 718 116 Q540 130 338 186 Z" fill="var(--swoosh)"/>
      <path class="photo-frame" d="M893 0 Q772 130 832 254" fill="none" stroke="var(--arc-orange)" stroke-width="7"/>
      <path class="drinks-photo" role="img" aria-label="Photo of bubble tea cups with pearls, fresh fruit and mint" d="M908 0 Q790 130 848 254 L1200 254 L1200 0 Z" fill="url(#drinks-tone)"/>
    </svg>

    <div class="brand">
      <span class="brand-dot"></span>
      <span class="brand-name">Plum Harbor</span>
    </div>

    <div class="cups-photo" role="img" aria-label="Photo of four bubble tea cups with straws and tapioca pearls"></div>

    <h1 class="headline">
      <span class="headline-fresh">Fresh</span>
      <span class="headline-product">BUBBLE TEA</span>
    </h1>
  </section>
</div>
</body>
</html>
```